Wedding ring tattoo

Left hand ring finger- size 11
Options to consider:
- Wedding Date: 3/7/92
- Wife initials: JAS
- My initials: TDS
Current ring inscription:
JAK+TDS Forever 3.7.92
My name: Tony
Wife name: Jane
Roman numerals
All black

```html
<!DOCTYPE html>
<html lang="en">
<head>
<meta charset="utf-8">
<title>Wedding Ring Tattoo – Tony &amp; Jane</title>
<link rel="stylesheet" href="https://fonts.googleapis.com/css2?family=EB+Garamond:wght@600&display=swap">
<style>
  :root {
    --ink: #000000;
    --paper: #ffffff;
  }
  html, body {
    margin: 0;
    padding: 0;
    width: 1200px;
    height: 1200px;
    overflow: hidden;
    background: var(--paper);
  }
  .canvas {
    display: block;
    width: 1200px;
    height: 1200px;
  }
  .band-text {
    font-family: "EB Garamond", "Times New Roman", serif;
    font-weight: 600;
    fill: var(--ink);
    font-size: 21px;
  }
  .monogram {
    font-family: "EB Garamond", "Times New Roman", serif;
    font-weight: 600;
    fill: var(--paper);
    font-size: 46px;
    letter-spacing: 1px;
  }
</style>
</head>
<body>
<svg class="canvas" viewBox="0 0 1100 1100" xmlns="http://www.w3.org/2000/svg">
  <defs>
    <g id="ring-band">
      <!-- band body with drop edge -->
      <path class="band-outline" fill="var(--ink)"
        d="M206 343 L905 343 Q898 360 904 372 L900 383 Q913 400 906 420 L910 438 Q905 446 895 446 L214 446 Q202 440 208 425 Q198 410 206 395 Q200 380 208 368 Q198 355 206 343 Z"/>
      <!-- pattern areas, solid black -->
      <g role="img" aria-label="Geometric triangle pattern band in solid black">
        <rect x="218" y="348" width="252" height="26" fill="var(--ink)"/>
        <rect x="218" y="400" width="252" height="30" fill="var(--ink)"/>
        <rect x="632" y="348" width="260" height="26" fill="var(--ink)"/>
        <rect x="632" y="400" width="260" height="30" fill="var(--ink)"/>
      </g>
      <!-- text strips -->
      <rect class="text-strip" x="215" y="374" width="258" height="26" fill="var(--paper)"/>
      <rect class="text-strip" x="632" y="374" width="264" height="26" fill="var(--paper)"/>
      <!-- center seal -->
      <circle cx="551" cy="389" r="82" fill="var(--ink)"/>
      <circle cx="551" cy="389" r="76" fill="var(--paper)"/>
      <circle cx="551" cy="389" r="71" fill="var(--ink)"/>
      <line x1="497" y1="350" x2="605" y2="350" stroke="var(--paper)" stroke-width="2.5"/>
      <line x1="497" y1="428" x2="605" y2="428" stroke="var(--paper)" stroke-width="2.5"/>
    </g>
  </defs>

  <!-- Ring band one: wife's initials -->
  <g class="ring ring-wife">
    <use href="#ring-band"/>
    <text class="band-text" x="220" y="394" textLength="232" lengthAdjust="spacingAndGlyphs">JAK+TDS FOREVER</text>
    <text class="monogram" x="551" y="405" text-anchor="middle">JAS</text>
    <text class="band-text" x="650" y="394" textLength="232" lengthAdjust="spacingAndGlyphs">TONY&#160;&#160;III.VII.XCII&#160;&#160;JANE</text>
  </g>

  <!-- Ring band two: husband's initials -->
  <g class="ring ring-husband" transform="translate(0 250)">
    <use href="#ring-band"/>
    <text class="band-text" x="220" y="394" textLength="232" lengthAdjust="spacingAndGlyphs">JAK+TDS FOREVER</text>
    <text class="monogram" x="551" y="405" text-anchor="middle">TDS</text>
    <text class="band-text" x="650" y="394" textLength="232" lengthAdjust="spacingAndGlyphs">TONY&#160;&#160;III.VII.XCII&#160;&#160;JANE</text>
  </g>
</svg>
</body>
</html>
```